New corporate e-mail signature

We need a new e-mail signature for our company that is clean and professional. The requests are attached in a document.

Target Market(s)

CFO, CTO, Controllers, leaders, decision-makers.

Industry/Entity Type

Information Technology

Colors

Designer to choose colors to be used in the design.

Requirements
Must have
• See the PowerPoint document.
• - keep it as simple as possible.
• - same style as our new website design
• - It has to look good in all e-mail readers, and on all surfaces.
Nice to have
• - Please also attach 'best practise' for how to use the signature.
Should not have
• See the PowerPoint document. Use our color palette.
• - Do not include photo!

```html
<!DOCTYPE html>
<html lang="en">
<head>
<meta charset="utf-8">
<title>Northgrid e-mail signatures</title>
<link href="https://fonts.googleapis.com/css2?family=Source+Sans+3:wght@400;600;700&display=swap" rel="stylesheet">
<style>
  :root {
    --navy: #0f3a73;
    --blue-top: #2a8fce;
    --blue-bottom: #0b2f63;
    --orange-top: #f39b4a;
    --orange-bottom: #ea5a5a;
    --orange-name: #f08a4b;
    --ink: #111111;
    --muted: #5a5a5a;
    --social-a: #3b5998;
    --social-b: #1da1f2;
    --social-c: #0077b5;
    --social-d: #c4161c;
    --paper: #ffffff;
  }
  * { box-sizing: border-box; margin: 0; padding: 0; }
  html, body { width: 818px; height: 1200px; overflow: hidden; background: var(--paper); }
  body { position: relative; font-family: "Source Sans 3", "Calibri", sans-serif; color: var(--ink); }

  .signature { position: absolute; left: 0; width: 818px; }
  .theme-blue { --grad: linear-gradient(180deg, var(--blue-top), var(--blue-bottom)); --accent: var(--navy); }
  .theme-orange { --grad: linear-gradient(180deg, var(--orange-top), var(--orange-bottom)); --accent: var(--orange-name); }

  /* logo variant */
  .brand-tile {
    position: absolute; left: 120px; top: 0; width: 128px; height: 128px;
    background: var(--grad);
    display: flex; align-items: center; justify-content: center;
  }
  .brand-name { color: #fff; font-weight: 700; font-size: 22px; letter-spacing: 0.2px; }
  .divider { position: absolute; width: 4px; background: var(--grad); }
  .with-logo .divider { left: 265px; top: 0; height: 128px; }

  .details { position: absolute; font-size: 17px; line-height: 24px; white-space: nowrap; }
  .with-logo .details { left: 285px; top: -8px; }
  .headline .person { color: var(--accent); font-weight: 700; font-size: 23px; }
  .headline .role { color: var(--muted); font-size: 20px; }
  .theme-orange.with-logo .headline .person { color: var(--orange-name); }
  .line b { font-weight: 700; }
  .accent-labels .line b { color: var(--navy); font-weight: 600; }
  .sep { margin: 0 12px; }

  .social { display: flex; gap: 3px; margin-top: 9px; }
  .social span { display: block; width: 21px; height: 21px; }
  .social.brand span:nth-child(1) { background: var(--social-a); }
  .social.brand span:nth-child(2) { background: var(--social-b); }
  .social.brand span:nth-child(3) { background: var(--social-c); }
  .social.brand span:nth-child(4) { background: var(--social-d); }
  .social.mono span { background: linear-gradient(180deg, #1d5e9c, var(--blue-bottom)); }
  .social.warm span { background: linear-gradient(180deg, var(--orange-top), #ee6f52); }

  /* name-left variant */
  .with-name .ident { position: absolute; left: 117px; top: -4px; }
  .with-name .ident .person { display: block; color: var(--navy); font-weight: 700; font-size: 23px; line-height: 30px; }
  .with-name .ident .role { display: block; color: var(--muted); font-size: 20px; line-height: 28px; }
  .with-name .divider { left: 292px; top: 0; height: 128px; }
  .with-name .details { left: 315px; top: -2px; }

  .set-count { position: absolute; right: 13px; bottom: 11px; color: var(--navy); font-weight: 700; font-size: 18px; }
</style>
</head>
<body>

<section class="signature with-logo theme-blue" style="top:66px">
  <div class="brand-tile"><span class="brand-name">northgrid</span></div>
  <div class="divider"></div>
  <div class="details">
    <p class="headline"><span class="person">Marten Olsby</span> <span class="role">- Head of Marketing</span></p>
    <p class="line">Office No: 123, Floor, Area, Street, City, Country</p>
    <p class="line"><b>T:</b> +47 900 12 345<span class="sep">|</span><b>F:</b> +47 400 55 210</p>
    <p class="line"><b>E:</b> post@northgrid.com<span class="sep">|</span><b>W:</b> www.northgrid.com</p>
    <div class="social brand"><span></span><span></span><span></span><span></span></div>
  </div>
</section>

<section class="signature with-logo theme-blue accent-labels" style="top:263px">
  <div class="brand-tile"><span class="brand-name">northgrid</span></div>
  <div class="divider"></div>
  <div class="details">
    <p class="headline"><span class="person">Marten Olsby</span> <span class="role">- Head of Marketing</span></p>
    <p class="line">Office No: 123, Floor, Area, Street, City, Country</p>
    <p class="line"><b>T:</b> +47 900 12 345<span class="sep">|</span><b>F:</b> +47 400 55 210</p>
    <p class="line"><b>E:</b> post@northgrid.com<span class="sep">|</span><b>W:</b> www.northgrid.com</p>
    <div class="social mono"><span></span><span></span><span></span><span></span></div>
  </div>
</section>

<section class="signature with-logo theme-orange" style="top:459px">
  <div class="brand-tile"><span class="brand-name">northgrid</span></div>
  <div class="divider"></div>
  <div class="details">
    <p class="headline"><span class="person">Marten Olsby</span> <span class="role">- Head of Marketing</span></p>
    <p class="line">Office No: 123, Floor, Area, Street, City, Country</p>
    <p class="line"><b>T:</b> +47 900 12 345<span class="sep">|</span><b>F:</b> +47 400 55 210</p>
    <p class="line"><b>E:</b> post@northgrid.com<span class="sep">|</span><b>W:</b> www.northgrid.com</p>
    <div class="social warm"><span></span><span></span><span></span><span></span></div>
  </div>
</section>

<section class="signature with-name theme-blue" style="top:655px">
  <div class="ident"><span class="person">Marten Olsby</span><span class="role">Head of Marketing</span></div>
  <div class="divider"></div>
  <div class="details">
    <p class="line">Office No: 123, Floor, Area, Street, City, Country</p>
    <p class="line"><b>T:</b> +47 900 12 345<span class="sep">|</span><b>F:</b> +47 400 55 210</p>
    <p class="line"><b>E:</b> post@northgrid.com</p>
    <p class="line"><b>W:</b> www.northgrid.com</p>
    <div class="social brand"><span></span><span></span><span></span><span></span></div>
  </div>
</section>

<section class="signature with-name theme-blue accent-labels" style="top:837px">
  <div class="ident"><span class="person">Marten Olsby</span><span class="role">Head of Marketing</span></div>
  <div class="divider"></div>
  <div class="details">
    <p class="line">Office No: 123, Floor, Area, Street, City, Country</p>
    <p class="line"><b>T:</b> +47 900 12 345<span class="sep">|</span><b>F:</b> +47 400 55 210</p>
    <p class="line"><b>E:</b> post@northgrid.com</p>
    <p class="line"><b>W:</b> www.northgrid.com</p>
    <div class="social mono"><span></span><span></span><span></span><span></span></div>
  </div>
</section>

<section class="signature with-name theme-orange" style="top:1019px">
  <div class="ident"><span class="person">Marten Olsby</span><span class="role">Head of Marketing</span></div>
  <div class="divider"></div>
  <div class="details">
    <p class="line">Office No: 123, Floor, Area, Street, City, Country</p>
    <p class="line"><b>T:</b> +47 900 12 345<span class="sep">|</span><b>F:</b> +47 400 55 210</p>
    <p class="line"><b>E:</b> post@northgrid.com</p>
    <p class="line"><b>W:</b> www.northgrid.com</p>
    <div class="social warm"><span></span><span></span><span></span><span></span></div>
  </div>
</section>

<p class="set-count">6 in 1</p>

</body>
</html>
```